New Energy Drink

*Name, Logo, Flatlay, and Y8 Mockup design of a new energy drink*
We are a current RTD (ready to drink) company looking to expand into the Energy market. We are not sure if we will stick with our parent company name or go a completely different direction. That's where you come in.
Get creative. Come up with a name, design a logo, and create the look and feel of our next big product. We want fun, bright, and forward-thinking designs. Don't think Kestrin and pavlune, but more along the lines of Jolve, Y8, and Frim as our proposed target market is in the same 18-25 demographic.
The only request is the Term "With Super Caffeine" appear somewhere on the visible label. A Y8 can render is attached. Please provide a Lay Flat and a Rendered Can together when submitting your designs.
FYI, the design brief is just a generic template. DO NOT USE the "grunge" or "brick" as a reference when creating your designs. We are offering a $1,000 prize to the winning designer. So please, really think this through. 1 great design is better than 5 quick designs. Good Luck!
18-25

```html
<!DOCTYPE html>
<html lang="en">
<head>
<meta charset="utf-8">
<title>Zu Mi Energy Drink – Lay Flat Label</title>
<link rel="stylesheet" href="https://fonts.googleapis.com/css2?family=Inter:wght@600;800&display=swap">
<style>
  :root {
    --paper: #ffffff;
    --trim: #1a1a1a;
    --cyan: #1ccfe8;
    --sky: #3f8cf0;
    --violet: #6a2cff;
    --purple: #8500ff;
    --orchid: #a812f2;
    --magenta: #cc2ae0;
    --ink-light: #ffffff;
  }
  * { margin: 0; padding: 0; box-sizing: border-box; }
  html, body {
    width: 1200px; height: 1010px;
    overflow: hidden;
    background: var(--paper);
    font-family: "Inter", Arial, sans-serif;
  }
  .artboard { position: relative; width: 1200px; height: 1010px; }
  .crop-marks { position: absolute; inset: 0; }
  .crop-marks line { stroke: var(--trim); stroke-width: 1; }
  .label {
    position: absolute;
    left: 166px; top: 234px;
    width: 863px; height: 539px;
    overflow: hidden;
  }
  .label-art { position: absolute; inset: 0; }
  .badge {
    position: absolute;
    left: 382px; top: 16px;
    width: 100px; height: 100px;
    overflow: visible;
  }
  .badge text {
    font-family: "Inter", Arial, sans-serif;
    font-weight: 600;
    font-size: 11px;
    letter-spacing: 2.4px;
    fill: var(--ink-light);
  }
  .brand {
    position: absolute;
    left: 0; right: 0; top: 176px;
    text-align: center;
    color: var(--ink-light);
    font-weight: 800;
    line-height: 1;
  }
  .brand-name {
    display: block;
    font-size: 116px;
    letter-spacing: 4px;
    line-height: 112px;
    margin-left: 2px;
  }
  .brand-tagline {
    display: block;
    font-size: 11px;
    font-weight: 600;
    letter-spacing: 0.3px;
    margin: -6px 0 2px;
  }
  .product {
    position: absolute;
    left: 0; right: 0; top: 490px;
    text-align: center;
    color: var(--ink-light);
  }
  .product-type {
    display: block;
    font-size: 21px;
    font-weight: 800;
    letter-spacing: -0.3px;
    line-height: 22px;
  }
  .product-volume {
    display: block;
    font-size: 11px;
    font-weight: 600;
    line-height: 14px;
  }
</style>
</head>
<body>
<main class="artboard">
  <svg class="crop-marks" width="1200" height="1010" aria-hidden="true">
    <line x1="167.5" y1="213" x2="167.5" y2="233"/>
    <line x1="426.5" y1="213" x2="426.5" y2="233"/>
    <line x1="771.5" y1="213" x2="771.5" y2="233"/>
    <line x1="1029.5" y1="213" x2="1029.5" y2="233"/>
    <line x1="146" y1="234.5" x2="166" y2="234.5"/>
    <line x1="146" y1="302.5" x2="166" y2="302.5"/>
    <line x1="146" y1="773.5" x2="166" y2="773.5"/>
    <line x1="1034" y1="234.5" x2="1054" y2="234.5"/>
    <line x1="1034" y1="302.5" x2="1054" y2="302.5"/>
    <line x1="1034" y1="773.5" x2="1054" y2="773.5"/>
  </svg>

  <section class="label">
    <svg class="label-art" width="863" height="539" viewBox="0 0 863 539"
         role="img" aria-label="Flowing liquid blobs with halftone dot pattern in cyan, violet and magenta">
      <defs>
        <linearGradient id="label-base" x1="0" y1="0" x2="0" y2="1">
          <stop offset="0" stop-color="var(--sky)"/>
          <stop offset="0.3" stop-color="var(--violet)"/>
          <stop offset="0.55" stop-color="var(--purple)"/>
          <stop offset="0.85" stop-color="var(--orchid)"/>
          <stop offset="1" stop-color="var(--magenta)"/>
        </linearGradient>
        <radialGradient id="cyan-glow-left" cx="0.2" cy="0" r="0.45">
          <stop offset="0" stop-color="var(--cyan)"/>
          <stop offset="1" stop-color="var(--cyan)" stop-opacity="0"/>
        </radialGradient>
        <radialGradient id="cyan-glow-right" cx="0.8" cy="0" r="0.3">
          <stop offset="0" stop-color="var(--cyan)"/>
          <stop offset="1" stop-color="var(--cyan)" stop-opacity="0"/>
        </radialGradient>
      </defs>
      <rect width="863" height="539" fill="url(#label-base)"/>
      <rect width="863" height="539" fill="url(#cyan-glow-left)"/>
      <rect width="863" height="539" fill="url(#cyan-glow-right)"/>
    </svg>

    <svg class="badge" viewBox="0 0 100 100" aria-label="With super caffeine">
      <defs>
        <path id="badge-ring" d="M50,91 A41,41 0 1,1 50.01,91"/>
      </defs>
      <circle cx="50" cy="50" r="30" fill="var(--ink-light)"/>
      <text><textPath href="#badge-ring" startOffset="11%">WITH SUPER CAFFEINE</textPath></text>
    </svg>

    <h1 class="brand">
      <span class="brand-name">ZU</span>
      <span class="brand-tagline">MAKE YOUR DAY!</span>
      <span class="brand-name">MI</span>
    </h1>

    <p class="product">
      <span class="product-type">ENERGY DRINK</span>
      <span class="product-volume">16 FL OZ (273ML)</span>
    </p>
  </section>
</main>
</body>
</html>
```